Business card design reauest

2 sided. White on both sides

Martin Oakhurst

Ho Chi Minh, Vietnam

Cell Phone / Whatsapp/ Wechat/Zalo
1-555-382-7194
Moakhurst@kvpartsline.vn
Www.kvpartsline.vn
Www.kvpartsline.com

Industry/Entity Type

Sofa and furniture and kitchen

Contact Information for Business Card

2 sided. White on both sides Martin Oakhurst Ho Chi Minh, Vietnam Cell Phone / Whatsapp/ Wechat/Zalo 1-555-382-7194 Moakhurst@kvpartsline.vn Www.kvpartsline.vn Www.kvpartsline.com

```html
<!DOCTYPE html>
<html lang="en">
<head>
<meta charset="utf-8">
<title>Keystone Valley Parts — Business Card</title>
<link href="https://fonts.googleapis.com/css2?family=Cinzel:wght@500&family=Montserrat:wght@500;700&display=swap" rel="stylesheet">
<style>
  :root {
    --brand-green: #0a9847;
    --ink: #1d1d1d;
    --paper: #ffffff;
    --stage: #e9e9e7;
    --rule-green: #129a4a;
  }
  * { box-sizing: border-box; margin: 0; padding: 0; }
  html, body { width: 1200px; height: 786px; overflow: hidden; }
  body {
    background: var(--stage);
    font-family: "Montserrat", Arial, sans-serif;
    position: relative;
  }
  .card {
    position: absolute;
    top: 238px;
    width: 540px;
    height: 310px;
    overflow: hidden;
    box-shadow: 0 6px 18px rgba(0,0,0,.18);
  }
  .card--front { left: 40px; background: var(--paper); }
  .card--back  { left: 620px; background: var(--brand-green); }

  .brand {
    font-family: "Cinzel", Georgia, serif;
    font-weight: 500;
    letter-spacing: .5px;
    line-height: 1.05;
    text-align: center;
    display: flex;
    align-items: center;
    gap: 10px;
  }
  .brand__square { width: 14px; height: 14px; flex: none; }

  .card--front .brand {
    position: absolute; right: 62px; top: 44px;
    color: var(--brand-green); font-size: 26px;
  }
  .card--front .brand__square { background: var(--brand-green); }

  .card--back .brand {
    position: absolute; left: 0; right: 0; top: 0; bottom: 0;
    justify-content: center;
    color: var(--paper); font-size: 40px;
  }
  .card--back .brand__square { background: var(--paper); width: 20px; height: 20px; }

  .divider {
    position: absolute; left: 28px; right: 40px; top: 158px;
    height: 2px; background: var(--rule-green);
  }
  .address {
    position: absolute; right: 28px; top: 194px;
    font-size: 12px; font-weight: 500; color: var(--ink);
    text-align: right; line-height: 1.35;
  }
  .person { position: absolute; left: 28px; top: 118px; }
  .person__name {
    font-weight: 700; font-size: 22px; color: var(--brand-green);
  }
  .person__city { font-size: 13px; font-weight: 500; color: var(--ink); margin-top: -2px; }

  .contacts {
    position: absolute; left: 28px; top: 176px;
    list-style: none; font-size: 13px; font-weight: 500; color: var(--ink);
  }
  .contacts li { display: flex; align-items: center; gap: 8px; height: 24px; }
  .contacts svg { flex: none; }
  .dots { display: flex; gap: 3px; }
  .dots span { width: 10px; height: 10px; border-radius: 50%; background: var(--brand-green); }

  .footer-band {
    position: absolute; left: 0; right: 0; bottom: 0; height: 20px;
    display: flex;
  }
  .footer-band__green { flex: 3; background: var(--brand-green); }
  .footer-band__dark  { flex: 1; background: var(--ink); }
</style>
</head>
<body>

<section class="card card--front" aria-label="Business card front">
  <div class="brand">
    <span class="brand__square"></span>
    <span>Keystone Valley<br>Parts</span>
  </div>

  <div class="person">
    <p class="person__name">Martin Oakhurst</p>
    <p class="person__city">Ho Chi Minh, Vietnam</p>
  </div>

  <div class="divider"></div>

  <p class="address">418 Harbor Mill Rd, #112<br>Fairhaven, OH 430519</p>

  <ul class="contacts">
    <li>
      <svg width="12" height="12" viewBox="0 0 24 24" aria-hidden="true"><path fill="#0a9847" d="M6.6 10.8a15.1 15.1 0 0 0 6.6 6.6l2.2-2.2a1 1 0 0 1 1-.25 11.4 11.4 0 0 0 3.6.57 1 1 0 0 1 1 1V20a1 1 0 0 1-1 1A17 17 0 0 1 3 4a1 1 0 0 1 1-1h3.5a1 1 0 0 1 1 1c0 1.25.2 2.45.57 3.57a1 1 0 0 1-.25 1z"/></svg>
      <span class="dots"><span></span><span></span><span></span></span>
      <span>1-555-382-7194</span>
    </li>
    <li>
      <svg width="12" height="12" viewBox="0 0 24 24" aria-hidden="true"><path fill="#0a9847" d="M2 5h20v14H2z"/><path fill="none" stroke="#fff" stroke-width="2" d="M2 5l10 8 10-8"/></svg>
      <span>Moakhurst@kvpartsline.vn</span>
    </li>
    <li>
      <svg width="12" height="12" viewBox="0 0 24 24" aria-hidden="true"><circle cx="12" cy="12" r="10" fill="#0a9847"/><path fill="none" stroke="#fff" stroke-width="1.6" d="M2 12h20M12 2c3 3 3 17 0 20M12 2c-3 3-3 17 0 20"/></svg>
      <span>Www.kvpartsline.vn</span>
    </li>
  </ul>

  <div class="footer-band">
    <div class="footer-band__green"></div>
    <div class="footer-band__dark"></div>
  </div>
</section>

<section class="card card--back" aria-label="Business card back">
  <div class="brand">
    <span class="brand__square"></span>
    <span>Keystone Valley<br>Parts</span>
  </div>
</section>

</body>
</html>
```